Menu Board 1000mmx500mm re-design

I would like to re-design exiting menu board 1000mmx500mm. Current board letters are bit to small to read. I would like to have pictures (attached) of the food offered on it and at the same time to create balance between pictures and size of the text to be easily readable. Fonts and colours are up to designer choice but prefer warm and bright colours rather anything dark.

Target Market(s)

Food industry

Industry/Entity Type

Food

Font styles to use
Other font styles liked:
• I leave font choice to designer

Colors
FFC000
F8CF3A
FAE287
FDF2CF
FEFAEE
F0912C
F2A743
F7CA91
FBE8D2
FDF5EE
EE7325
F08F49
F5BC92
FAE3D3
FDF4ED

Requirements
Must have
• Pictures + Text
Nice to have
• Balance between images and text.
Should not have
• Can't think of any

```html
<!DOCTYPE html>
<html lang="en">
<head>
<meta charset="utf-8">
<title>Menu Board</title>
<link href="https://fonts.googleapis.com/css2?family=Poppins:wght@400;700;800;900&family=Great+Vibes&family=Anton&display=swap" rel="stylesheet">
<style>
  :root{
    --orange:#e8571a;
    --orange-bright:#f7842b;
    --orange-text:#e85a17;
    --yellow:#ffc000;
    --panel:#f1f0f2;
    --ink:#1f1d1e;
    --page:#ececec;
    --white:#ffffff;
    --green:#1f6b3a;
  }
  *{box-sizing:border-box;margin:0;padding:0}
  html,body{width:1200px;height:1200px;overflow:hidden;background:var(--page)}
  .board{position:absolute;left:320px;top:40px;width:560px;height:1120px;background:var(--panel);overflow:hidden;font-family:"Poppins",sans-serif;color:var(--ink)}
  .board-shapes{position:absolute;inset:0}
  .dish{position:absolute;left:26px;width:138px;height:138px;border-radius:50%;background:var(--white);border:1.5px solid var(--orange-bright);padding:5px}
  .dish span{display:block;width:100%;height:100%;border-radius:50%}
  .dish-chicken-rice span{background:radial-gradient(circle at 45% 45%,#f3efe2 0,#c99a5e 35%,#6b3f22 60%,#dfe3ea 75%)}
  .dish-potatoes span{background:radial-gradient(circle at 50% 50%,#f0b85a 0,#d88a35 40%,#8a4a1d 70%,#2b2020 100%)}
  .dish-ciabatta span{background:linear-gradient(180deg,#e9e8ee 0,#d9a566 35%,#4d7a2a 52%,#e6c593 62%,#7a4a26 75%,#e6e6ec 100%)}
  .dish-wrap span{background:radial-gradient(circle at 50% 50%,#e8d9a8 0,#6c8f3a 35%,#c9442f 55%,#e6d6b0 75%,#bfb8b0 100%)}
  .menu-title{position:absolute;left:208px;top:180px;font-family:"Great Vibes",cursive;font-size:104px;line-height:1;color:var(--orange-text)}
  .item{position:absolute;left:210px;width:337px}
  .item-name{font-weight:800;font-size:28px;line-height:32px;letter-spacing:-.2px;white-space:nowrap}
  .item-row{display:flex;align-items:flex-end;gap:8px;margin-top:3px}
  .item-desc{flex:1;font-size:18px;line-height:22px;font-weight:400}
  .leader{letter-spacing:1px}
  .price{flex:0 0 70px;height:29px;background:var(--orange-text);color:var(--ink);font-weight:700;font-size:21px;line-height:29px;text-align:center}
  .item-line{display:flex;align-items:center;gap:8px}
  .item-line .item-name{flex:1;overflow:hidden}
  .footer{position:absolute;left:0;top:1012px;width:560px;height:84px;background:var(--white)}
  .sauces-label{position:absolute;left:33px;top:18px;font-family:"Anton",sans-serif;font-size:40px;line-height:48px;color:var(--ink);letter-spacing:.5px}
  .sauces-divider{position:absolute;left:159px;top:20px;width:1.5px;height:50px;background:var(--ink)}
  .sauce{position:absolute;font-weight:800;font-size:22px;line-height:26px;color:var(--orange-text);white-space:nowrap}
  .base-stripe{position:absolute;left:0;top:1092px;width:560px;height:28px;background:linear-gradient(90deg,var(--green),#7a6a1e 35%,var(--orange) 65%,var(--orange));border-top:4px solid var(--yellow)}
</style>
</head>
<body>
<main class="board">
  <svg class="board-shapes" width="560" height="1120" viewBox="0 0 560 1120">
    <defs>
      <linearGradient id="photoTone" x1="0" y1="0" x2="1" y2="1">
        <stop offset="0" stop-color="#7a3d1c"/>
        <stop offset=".4" stop-color="#d9953f"/>
        <stop offset=".7" stop-color="#f0b85e"/>
        <stop offset="1" stop-color="#c0702c"/>
      </linearGradient>
      <radialGradient id="orangeGlow" cx=".5" cy=".45" r=".7">
        <stop offset="0" stop-color="#fb8a2e"/>
        <stop offset="1" stop-color="#e6520f"/>
      </radialGradient>
    </defs>
    <rect role="img" aria-label="Roasted potatoes with a sprig of rosemary" x="0" y="0" width="560" height="330" fill="url(#photoTone)"/>
    <path d="M0,318 C60,285 130,262 197,252 L197,1012 L0,1012 Z" fill="url(#orangeGlow)"/>
    <path d="M197,252 C300,238 380,272 460,256 C510,246 540,226 560,205 L560,1012 L197,1012 Z" fill="#f1f0f2"/>
    <path d="M197,252 C300,238 380,272 460,256 C510,246 540,226 560,205" fill="none" stroke="#ee6a1c" stroke-width="8"/>
    <rect x="188" y="252" width="9" height="760" fill="#ffc000"/>
  </svg>

  <div class="dish dish-chicken-rice" role="img" aria-label="Roast chicken with veggie rice" style="top:260px"><span></span></div>
  <div class="dish dish-potatoes" role="img" aria-label="Roasted potatoes" style="top:448px"><span></span></div>
  <div class="dish dish-ciabatta" role="img" aria-label="Chicken ciabatta with rocket" style="top:637px"><span></span></div>
  <div class="dish dish-wrap" role="img" aria-label="Chicken wrap with vegetables" style="top:828px"><span></span></div>

  <h1 class="menu-title">Menu</h1>

  <section class="item" style="top:300px">
    <h2 class="item-name">CIABATTA</h2>
    <div class="item-row"><p class="item-desc">Roti Chicken, Rucola, Caramelized Tomato, Fresh Onion<span class="leader">.........................</span></p><span class="price">£6</span></div>
  </section>
  <section class="item" style="top:413px">
    <h2 class="item-name">WRAP</h2>
    <div class="item-row"><p class="item-desc">Roti Chicken, Crunchy Slaw, Tomato, Fresh Onion &amp; Sauce of your Choice<span class="leader">......</span></p><span class="price">£7</span></div>
  </section>
  <section class="item" style="top:527px">
    <h2 class="item-name">BEETROOT WRAP</h2>
    <div class="item-row"><p class="item-desc">Roti Chicken, Crunchy Slaw, Tomato, Fresh Onion &amp; Sauce of your Choice<span class="leader">......</span></p><span class="price">£8</span></div>
  </section>
  <section class="item" style="top:646px">
    <h2 class="item-name">1/4 Chicken Box</h2>
    <div class="item-row"><p class="item-desc">Roti Chicken, Veggie Rice &amp; Salad <span class="leader">...........................</span></p><span class="price">£9</span></div>
  </section>
  <section class="item" style="top:747px">
    <h2 class="item-name">1/2 Chicken Box</h2>
    <div class="item-row"><p class="item-desc">Roti Chicken, Veggie Rice &amp; Salad <span class="leader">....................</span></p><span class="price">£14</span></div>
  </section>
  <section class="item" style="top:840px">
    <h2 class="item-name">Roasted Potatoes</h2>
    <div class="item-row"><p class="item-desc">Thyme &amp; Garlic <span class="leader">.................</span></p><span class="price">£2.5</span></div>
  </section>
  <section class="item" style="top:917px">
    <div class="item-line"><h2 class="item-name">WATER ...............</h2><span class="price">£1</span></div>
  </section>
  <section class="item" style="top:967px">
    <div class="item-line"><h2 class="item-name">CAN &amp; JUICES ....</h2><span class="price">£1.8</span></div>
  </section>

  <footer class="footer">
    <h2 class="sauces-label">SAUCES</h2>
    <span class="sauces-divider"></span>
    <span class="sauce" style="left:179px;top:16px">SIGNATURE</span>
    <span class="sauce" style="left:349px;top:16px">BBQ</span>
    <span class="sauce" style="left:434px;top:16px">PIRI PIRI</span>
    <span class="sauce" style="left:179px;top:43px">SWEET CHILLI</span>
    <span class="sauce" style="left:349px;top:43px">GARLIC MAYO</span>
  </footer>
  <div class="base-stripe"></div>
</main>
</body>
</html>
```